Marlow Hire Business Card for recruitment company

We are looking for a Business Card Design that incorporates our personal details and our busines name and logo. We are a specialized search consultancy that recruit Property and Construction professionals.
We would like a business card that stands out and is appealing to the Construction and Property industry as well.

Target Market(s)

people in the construction and property industry

Contact Information for Business Card

Business Name and logo

Font styles to use
Serif

Colors
0094D4
00A9DD
6FCCEA
C7EBF8
E9F6FB

Requirements
Must have
• Business name and logo as well as contact details
Should not have
• No photos of us please

```html
<!DOCTYPE html>
<html lang="en">
<head>
<meta charset="utf-8">
<title>Marlow Hire – Business Card</title>
<link rel="stylesheet" href="https://fonts.googleapis.com/css2?family=Zilla+Slab:wght@400;700&family=Roboto:wght@300;500&family=Roboto+Condensed:wght@700&display=swap">
<style>
  :root {
    --navy: #06364f;
    --paper: #ffffff;
    --backdrop: #f2f3f4;
    --pattern-light: #7f9a9c;
  }
  * { margin: 0; padding: 0; box-sizing: border-box; }
  html, body { width: 1200px; height: 857px; overflow: hidden; }
  body { background: var(--backdrop); position: relative; font-family: "Zilla Slab", serif; color: var(--navy); }

  .card { position: absolute; left: 346px; width: 508px; height: 289px; }
  .card--front { top: 112px; background: var(--paper); border: 7px solid var(--navy); border-bottom-width: 8px; }
  .card--front::before {
    content: ""; position: absolute; inset: 3px; border: 1.5px solid var(--navy);
  }
  .card--back {
    top: 455px; height: 290px;
    background: radial-gradient(ellipse at 50% 55%, #2e5765 0%, #103f55 55%, var(--navy) 100%);
  }

  .brand {
    position: absolute; left: 44px; top: 38px;
    font-family: "Roboto", sans-serif; font-weight: 300;
    font-size: 33px; letter-spacing: 1px; line-height: 1; text-transform: uppercase;
  }
  .person__name {
    position: absolute; left: 44px; top: 112px;
    font-weight: 700; font-size: 27px; line-height: 1;
  }
  .person__role {
    position: absolute; left: 45px; top: 141px;
    font-family: "Roboto", sans-serif; font-weight: 500; font-size: 12px; line-height: 1;
  }
  .contact { position: absolute; left: 42px; display: flex; align-items: center; gap: 8px; font-size: 16.5px; line-height: 1; }
  .contact--phone { top: 169px; }
  .contact--email { top: 193px; }
  .contact svg { width: 19px; height: 19px; flex: none; }
  .web {
    position: absolute; right: 19px; top: 196px;
    font-family: "Roboto Condensed", sans-serif; font-weight: 700; font-size: 14.5px; line-height: 1;
  }
  .divider { position: absolute; left: 18px; right: 19px; top: 231px; height: 1px; background: var(--navy); }
  .address { position: absolute; left: 18px; right: 19px; top: 246px; font-size: 15.6px; line-height: 1; text-align: justify; text-align-last: justify; }
</style>
</head>
<body>
  <section class="card card--front" aria-label="Business card front">
    <div class="brand">Marlow Hire</div>
    <h1 class="person__name">Clara Hensley</h1>
    <p class="person__role">Director | Senior Search Consultant</p>
    <p class="contact contact--phone">
      <svg viewBox="0 0 20 20" aria-hidden="true"><circle cx="10" cy="10" r="9" fill="none" stroke="currentColor" stroke-width="1.3"/><path d="M7.2 5.2l1.6 2.4-1 1.1c.6 1.3 1.4 2.1 2.6 2.7l1.1-1 2.3 1.6-.8 1.6c-3.4-.2-6.4-3.3-6.6-6.7z" fill="currentColor"/></svg>
      +64 27 555 0148
    </p>
    <p class="contact contact--email">
      <svg viewBox="0 0 20 20" aria-hidden="true"><circle cx="10" cy="10" r="9" fill="none" stroke="currentColor" stroke-width="1.3"/><rect x="5" y="6.5" width="10" height="7" rx="1" fill="currentColor"/><path d="M5.5 7.2l4.5 3.6 4.5-3.6" fill="none" stroke="#fff" stroke-width="1"/></svg>
      clara@marlowhire.nz
    </p>
    <p class="web">WWW.MARLOWHIRE.NZ</p>
    <div class="divider"></div>
    <p class="address">12 Harbour View Lane, Northcote, Auckland, 0627, New Zealand</p>
  </section>

  <section class="card card--back" role="img" aria-label="Business card back: repeating pattern of the brand symbol in soft silver on deep navy"></section>
</body>
</html>
```